Flyer for corporate discount for dog daycare

I own a dog daycare with a large corporate down the road. I am working with the President of the company to offer their employees a discount for my services, Dog Daycare, Overnight Care, Grooming Salon & Spa and Retail. The design should be professional but also have a soft side as people view their dogs similar to human children.

I attached my logo along with our grooming brochure for reference on colors we've been using.

At a minimum the flyer must contain the following information:
Name: The Wagtail Lodge
web address: www.PawHavenStays.example
phone number: 920-555-0148
Address: 4872 Larchmont Lane
Google Map of our location

Title of flyer/program: Corporate V.I.P. (Very Important Pooch) (Can be creative with how to include this such as, Welcome to our Corporate. . .. etc.)

The program offer is: 5% discount
My services: Dog Daycare, Overnight Care, Grooming Salon & Spa and Retail

Target Market(s)

corporate employees, male and female, age 24+

Industry/Entity Type

Daycare

Requirements
Must have
• Must be easy to read and inviting.
Nice to have
• Nice photo dogs playing or inviting photo of dog.
Should not have
• cartoon feel

```html
<!DOCTYPE html>
<html lang="en">
<head>
<meta charset="utf-8">
<title>Corporate V.I.P. Flyer – The Wagtail Lodge</title>
<link href="https://fonts.googleapis.com/css2?family=Oswald:wght@400;500;700&family=Open+Sans:wght@400;700&family=Kalam:wght@400&display=swap" rel="stylesheet">
<style>
  :root {
    --green: #8cc63f;
    --green-dark: #5f9a22;
    --olive: #9aa83a;
    --teal: #6bbcc6;
    --teal-pale: #cfe9ee;
    --ink: #4a4a48;
    --ink-dark: #333331;
    --white: #ffffff;
    --sky: #eef6f8;
  }
  * { margin: 0; padding: 0; box-sizing: border-box; }
  html, body { width: 898px; height: 1200px; overflow: hidden; background: var(--white); }
  .flyer {
    position: relative; width: 898px; height: 1200px; overflow: hidden;
    font-family: "Open Sans", sans-serif;
    background: linear-gradient(180deg, var(--sky) 0%, #f7fbfc 60%, #e6f2f4 100%);
  }
  .stripes { position: absolute; inset: 0; }
  .header-photo {
    position: absolute; left: 0; top: 0; width: 898px; height: 240px;
    background: linear-gradient(100deg, #e9ecec 0%, #b9bfc3 45%, #7e868c 100%);
  }
  .brand {
    position: absolute; left: 34px; top: 34px; display: flex; align-items: center; gap: 12px;
    background: var(--white); padding: 14px 18px; border-radius: 4px;
  }
  .brand-square { width: 34px; height: 34px; background: var(--green); }
  .brand-name { font-family: "Oswald", sans-serif; font-weight: 500; font-size: 30px; color: var(--ink-dark); line-height: 1; }
  .services {
    position: absolute; right: 40px; top: 38px; text-align: right;
    color: var(--white); font-weight: 700; font-size: 26px; line-height: 1.3;
    text-shadow: 0 1px 3px rgba(0,0,0,.35);
  }
  .pooch-band {
    position: absolute; left: 250px; top: 245px; width: 648px; height: 60px;
    background: var(--green); display: flex; align-items: center; justify-content: center;
    font-family: "Oswald", sans-serif; font-size: 38px; color: var(--white); gap: 10px;
  }
  .pooch-band em { font-style: normal; color: var(--ink-dark); }
  .dog-photo {
    position: absolute; left: 20px; top: 265px; width: 400px; height: 600px;
    background: radial-gradient(ellipse at 50% 45%, #b9794a 0%, #9a5f35 55%, rgba(154,95,53,0) 72%);
  }
  .title-corporate {
    position: absolute; left: 440px; top: 360px; width: 420px; text-align: center;
    font-family: "Oswald", sans-serif; font-weight: 400; font-size: 80px; color: var(--olive); letter-spacing: 2px;
  }
  .title-vip {
    position: absolute; left: 420px; top: 430px; width: 460px; text-align: center;
    font-family: "Oswald", sans-serif; font-weight: 700; font-size: 210px; line-height: 1; color: var(--ink);
  }
  .title-sub {
    position: absolute; left: 430px; top: 660px; width: 450px; text-align: center;
    font-family: "Kalam", cursive; font-size: 40px; color: var(--ink);
  }
  .offer-figure {
    position: absolute; left: 450px; top: 700px; width: 420px; text-align: center;
    font-family: "Oswald", sans-serif; font-weight: 700; font-size: 250px; line-height: 1;
    color: var(--green); text-shadow: 6px 6px 0 var(--green-dark), 12px 12px 0 #4b7d18;
  }
  .offer-band {
    position: absolute; left: 450px; top: 920px; width: 448px; height: 64px;
    background: var(--green); color: var(--white); font-family: "Oswald", sans-serif;
    font-weight: 700; font-size: 48px; letter-spacing: 3px; display: flex; align-items: center; justify-content: center;
  }
  .map {
    position: absolute; left: 470px; top: 990px; width: 400px; height: 100px;
    background: linear-gradient(135deg, #e8eddc 0%, #dfe8e2 100%); border: 3px solid var(--white);
  }
  .contact { position: absolute; left: 480px; color: var(--white); font-weight: 700; font-size: 28px; display: flex; align-items: center; gap: 12px; }
  .contact-address { top: 1100px; }
  .contact-phone { top: 1145px; }
  .contact-strip { position: absolute; left: 450px; top: 1090px; width: 448px; height: 110px; background: var(--green); }
  .get-in-touch { position: absolute; left: 30px; top: 855px; width: 200px; height: 180px; }
  .get-in-touch span {
    position: absolute; left: 0; top: 40px; width: 190px; text-align: center;
    font-family: "Kalam", cursive; font-size: 40px; line-height: 1.05; color: var(--white); transform: rotate(-10deg);
  }
  .website {
    position: absolute; left: 30px; top: 1070px; font-family: "Oswald", sans-serif; font-weight: 700;
    font-size: 40px; color: var(--green-dark);
  }
</style>
</head>
<body>
<div class="flyer">
  <svg class="stripes" width="898" height="1200" aria-hidden="true">
    <polygon points="300,305 520,305 180,1200 0,1200 0,1050" fill="#dcedf1"/>
    <polygon points="620,305 760,305 560,1200 420,1200" fill="#e4f1f4"/>
    <polygon points="0,1110 898,980 898,1200 0,1200" fill="#d3eaee" opacity=".6"/>
  </svg>

  <div class="header-photo" role="img" aria-label="Photo of a happy white dog smiling"></div>
  <div class="brand"><span class="brand-square"></span><span class="brand-name">The Wagtail Lodge</span></div>
  <div class="services">Dog Daycare<br>Overnight Care<br>Grooming Salon &amp; Spa<br>and more...</div>

  <div class="pooch-band"><em>YOUR POOCH</em> joined yet?</div>

  <div class="dog-photo" role="img" aria-label="Photo of a boxer dog sitting and looking at the camera"></div>

  <div class="title-corporate">CORPORATE</div>
  <div class="title-vip">V.I.P</div>
  <div class="title-sub">(Very Important Pooch)</div>

  <div class="offer-figure">5%</div>
  <div class="offer-band">DISCOUNT</div>

  <div class="contact-strip"></div>
  <div class="map" role="img" aria-label="Street map showing the location of The Wagtail Lodge"></div>
  <div class="contact contact-address">
    <svg width="22" height="30" viewBox="0 0 22 30" aria-hidden="true"><path d="M11 0C5 0 0 5 0 11c0 8 11 19 11 19s11-11 11-19C22 5 17 0 11 0z" fill="#fff"/><circle cx="11" cy="11" r="4" fill="#8cc63f"/></svg>
    4872 Larchmont Lane
  </div>
  <div class="contact contact-phone">
    <svg width="26" height="26" viewBox="0 0 24 24" aria-hidden="true"><path d="M6.6 10.8a15 15 0 0 0 6.6 6.6l2.2-2.2c.3-.3.7-.4 1-.2 1.1.4 2.3.6 3.6.6.6 0 1 .4 1 1V20c0 .6-.4 1-1 1A17 17 0 0 1 3 4c0-.6.4-1 1-1h3.5c.6 0 1 .4 1 1 0 1.3.2 2.5.6 3.6.1.3 0 .7-.2 1z" fill="#fff"/></svg>
    920-555-0148
  </div>

  <div class="get-in-touch">
    <svg width="200" height="180" viewBox="0 0 200 180" aria-hidden="true">
      <circle cx="95" cy="85" r="82" fill="#6bbcc6"/>
      <polygon points="40,140 20,178 80,158" fill="#6bbcc6"/>
    </svg>
    <span>Get in<br>touch</span>
  </div>

  <div class="website">PawHavenStays.example</div>
</div>
</body>
</html>
```